Business cards - KESTO Roofing & Siding

We need simple business cards made up for our Roofing & Siding business based in Calgary Alberta.
The logo on one side of the card and potentially our slogan "Built with trust, verified by time".
The other side could have:
-A small logo
-Rep name:
-Rep cell phone:
-Rep email:
-Office phone: 403-386-2049
-Website: PrairieShinglePros.com

We would like to incorporate the colours from our logo, especially the lite blue on the jpeg file. I have attached the ai file and jpeg file. We like the colours better on the jpeg file.

I do not require a money back guarantee

```html
<!DOCTYPE html>
<html lang="en">
<head>
<meta charset="UTF-8">
<title>KESTO Roofing &amp; Siding – Business Cards</title>
<link rel="stylesheet" href="https://fonts.googleapis.com/css2?family=Montserrat:wght@400;500;600&display=swap">
<style>
  :root {
    --ink: #1b1b1b;
    --paper: #ffffff;
    --sky: #1e8ff0;
    --sky-deep: #1670c4;
    --stage: #d9dadc;
    --muted: #4a4a4a;
  }
  * { box-sizing: border-box; margin: 0; padding: 0; }
  html, body { width: 1200px; height: 1200px; overflow: hidden; }
  body {
    background: var(--stage);
    font-family: "Montserrat", Arial, sans-serif;
    position: relative;
  }
  .card {
    position: absolute;
    left: 120px;
    width: 960px;
    height: 549px;
    border-radius: 34px;
    overflow: hidden;
    box-shadow: 0 10px 30px rgba(0,0,0,.25);
  }
  .card--contact { top: 40px; background: var(--paper); }
  .card--brand { top: 611px; background: var(--ink); }

  .contact-panel { position: absolute; inset: 0; }

  .rep {
    position: absolute;
    left: 70px;
    top: 190px;
    padding-left: 26px;
    border-left: 8px solid var(--sky);
  }
  .rep__name {
    color: var(--sky);
    font-size: 50px;
    font-weight: 600;
    letter-spacing: 1px;
    line-height: 1;
  }
  .rep__title {
    color: var(--paper);
    font-size: 24px;
    font-weight: 500;
    margin-top: 6px;
  }
  .details {
    position: absolute;
    left: 104px;
    top: 330px;
    list-style: none;
  }
  .details li {
    display: flex;
    align-items: center;
    gap: 18px;
    color: var(--paper);
    font-size: 25px;
    line-height: 1;
    height: 44px;
  }
  .details svg { width: 28px; height: 28px; flex: none; }

  .brand {
    position: absolute;
    display: flex;
    align-items: center;
    gap: 18px;
  }
  .brand__mark { background: var(--sky); flex: none; }
  .brand__name {
    font-weight: 600;
    letter-spacing: 1px;
  }

  .card--contact .brand {
    left: 600px;
    width: 330px;
    top: 100px;
    flex-direction: column;
    gap: 16px;
  }
  .card--contact .brand__mark { width: 34px; height: 34px; }
  .card--contact .brand__name {
    color: var(--ink);
    font-size: 32px;
    line-height: 1.2;
    text-align: center;
  }

  .card--brand .brand { left: 50%; top: 50%; transform: translate(-50%, -50%); }
  .card--brand .brand__name { color: var(--paper); font-size: 44px; white-space: nowrap; }
  .card--brand .brand__mark { width: 42px; height: 42px; }
</style>
</head>
<body>

<section class="card card--contact">
  <svg class="contact-panel" viewBox="0 0 960 549" aria-hidden="true">
    <polygon points="0,0 370,0 532,215 572,549 0,549" fill="var(--ink)"/>
    <polyline points="384,0 546,212 586,549" fill="none" stroke="var(--sky)" stroke-width="9"/>
  </svg>

  <div class="rep">
    <p class="rep__name">JOHN DOE</p>
    <p class="rep__title">CEO | FOUNDER</p>
  </div>

  <ul class="details">
    <li>
      <svg viewBox="0 0 24 24"><rect x="6" y="2" width="12" height="20" rx="2" fill="none" stroke="var(--sky)" stroke-width="2"/><line x1="10" y1="18" x2="14" y2="18" stroke="var(--sky)" stroke-width="2"/></svg>
      403-386-2049
    </li>
    <li>
      <svg viewBox="0 0 24 24"><path d="M6.6 10.8a15 15 0 0 0 6.6 6.6l2.2-2.2a1 1 0 0 1 1-.25 11.4 11.4 0 0 0 3.6.57 1 1 0 0 1 1 1V20a1 1 0 0 1-1 1A17 17 0 0 1 3 4a1 1 0 0 1 1-1h3.5a1 1 0 0 1 1 1c0 1.250.2 2.45.57 3.57a1 1 0 0 1-.25 1z" fill="var(--sky)"/></svg>
      403-386-2049
    </li>
    <li>
      <svg viewBox="0 0 24 24"><rect x="2" y="5" width="20" height="14" fill="var(--sky)"/><polyline points="2,5 12,13 22,5" fill="none" stroke="var(--ink)" stroke-width="2"/></svg>
      rep@prairieshinglepros.com
    </li>
    <li>
      <svg viewBox="0 0 24 24"><circle cx="12" cy="12" r="10" fill="none" stroke="var(--sky)" stroke-width="2"/><ellipse cx="12" cy="12" rx="4" ry="10" fill="none" stroke="var(--sky)" stroke-width="1.6"/><line x1="2" y1="12" x2="22" y2="12" stroke="var(--sky)" stroke-width="1.6"/></svg>
      prairieshinglepros.com
    </li>
  </ul>

  <div class="brand">
    <span class="brand__mark"></span>
    <span class="brand__name">KESTO Roofing<br>&amp; Siding</span>
  </div>
</section>

<section class="card card--brand">
  <div class="brand">
    <span class="brand__mark"></span>
    <span class="brand__name">KESTO Roofing &amp; Siding</span>
  </div>
</section>

</body>
</html>
```